STATIONARY DESIGN TO INCLUDE-Biz Card, Letterhead, Envelope & Email Signature
MAPLEGATE ELECTRIC-use pre designed logo
Simple
Paula Winter
1865 Quillon Ridge San Antonio. TX 78299
210.555.0187 x240
pwinter@qbn.example
www.qbn.example
Please design the biz card with an all white background and square edges.... We have multiple offices but our main office is in Houston TX and for our industry Houston is huge. So, we would like it to state somewhere "Corporate Headquarters Houston TX"..... Lastly, please interchange this on the card because we are not sure if we want this yet, and you can put it wherever you believe it looks best (front or back). We would like it to also say "ISO 9001 Certified Quality Management System".
Please place the symbol from our logo on the back of our biz cards Also, include the website "www.qbn.example"

```html
<!DOCTYPE html>
<html lang="en">
<head>
<meta charset="utf-8">
<title>Maplegate Electric Stationery</title>
<link rel="stylesheet" href="https://fonts.googleapis.com/css2?family=Open+Sans:wght@400;700;800&family=Dancing+Script&display=swap">
<style>
:root{
  --navy:#1b4f9c;
  --blue:#2f8fd8;
  --sky:#8cc7f0;
  --green:#5aa83c;
  --ink:#333;
  --muted:#777;
  --paper:#fff;
  --stage:#e9e9e9;
  --steel-a:#f4f5f7;
  --steel-b:#b9bec6;
}
*{box-sizing:border-box;margin:0;padding:0}
html,body{width:1200px;height:857px;overflow:hidden}
body{background:var(--stage);font-family:"Open Sans",Arial,sans-serif;color:var(--ink);position:relative}
.piece{position:absolute;background:var(--paper);box-shadow:0 2px 6px rgba(0,0,0,.25);overflow:hidden}
.swoosh{position:absolute;pointer-events:none}

/* brand lockup */
.brand{display:flex;align-items:center;gap:5px}
.brand-dot{width:14px;height:14px;border-radius:50%;background:var(--blue);flex:none}
.brand-name{font-weight:800;color:var(--navy);font-size:11px;letter-spacing:.3px;white-space:nowrap}
.brand-sub{font-size:5px;color:var(--muted);margin-top:2px;line-height:1.3}
.brand-mid .brand-name{font-size:8.5px}
.brand-mid .brand-dot{width:11px;height:11px}
.brand-compact{gap:4px}
.brand-compact .brand-name{font-size:6.5px;letter-spacing:.2px}
.brand-compact .brand-dot{width:9px;height:9px}

/* letterhead */
.letterhead{padding:18px 22px;font-size:5.2px;line-height:1.45}
.letterhead .head{display:flex;justify-content:space-between;align-items:flex-start;margin-bottom:22px;position:relative;z-index:1}
.contact-block{font-size:5px;color:var(--navy);line-height:1.5;text-align:left}
.letter-body{position:relative;z-index:1}
.letter-body p{margin-bottom:6px}
.signature{font-family:"Dancing Script",cursive;font-size:11px;color:var(--navy);margin:4px 0 2px}
.footer-line{position:absolute;left:22px;bottom:14px;font-size:4.6px;color:var(--muted);z-index:1}

/* business card */
.card{padding:10px 12px;font-size:5.6px;line-height:1.45}
.card .holder{font-weight:700;font-size:7px;color:var(--navy)}
.card .role{color:var(--muted);margin-bottom:4px}
.card .details{color:var(--navy)}
.card .hq{position:absolute;bottom:8px;left:12px;font-size:5px;color:var(--green);font-weight:700}
.card .iso{position:absolute;bottom:8px;right:10px;font-size:4.6px;color:var(--muted);text-align:right;width:70px;line-height:1.3}
.card-back{display:flex;flex-direction:column;align-items:center;justify-content:center;gap:5px}
.card-back .big-dot{width:26px;height:26px;border-radius:50%;background:var(--blue)}
.card-back .web{font-size:6px;color:var(--navy)}
.card-steel{background:linear-gradient(135deg,var(--steel-a),var(--steel-b))}

/* envelope */
.envelope{padding:14px 18px}
.envelope .recipient{position:absolute;left:52%;top:52%;font-size:6px;line-height:1.6;color:var(--ink)}
.envelope-small{padding:6px 8px}
.envelope-small .brand-name{font-size:7px}
.envelope-small .brand-dot{width:9px;height:9px}
</style>
</head>
<body>

<!-- Letterhead, left: plain -->
<section class="piece letterhead" style="left:24px;top:14px;width:340px;height:470px">
  <div class="head">
    <div>
      <div class="brand"><span class="brand-dot"></span><span class="brand-name">MAPLEGATE ELECTRIC</span></div>
      <div class="brand-sub">1865 Quillon Ridge San Antonio. TX 78299<br>210.555.0187 x240 · www.qbn.example</div>
    </div>
  </div>
  <div class="letter-body">
    <p>Date</p>
    <p>Name of Recipient<br>Address</p>
    <p>Dear Sir/Madam</p>
    <p>We are pleased to confirm the scheduled electrical service for your facility. Our licensed crew will arrive on the agreed date and complete the inspection, panel upgrades and safety testing. A detailed report will follow within two business days, along with recommendations for any further work required.</p>
    <p>Should you have questions about the schedule or scope, please contact our office directly. We value your trust and look forward to serving you.</p>
    <p>Sincerely</p>
    <div class="signature">Paula Winter</div>
    <p>Paula Winter<br>VP Sales &amp; Marketing</p>
  </div>
</section>

<!-- Letterhead, middle: with swoosh bands -->
<section class="piece letterhead" style="left:400px;top:36px;width:400px;height:500px">
  <svg class="swoosh" style="left:0;top:0" width="400" height="70" viewBox="0 0 400 70">
    <path d="M0 0H400V8C300 8 160 10 60 40C30 50 10 62 0 70Z" fill="var(--sky)"/>
    <path d="M0 0H400V4C290 4 150 6 50 30C25 36 10 46 0 54Z" fill="var(--blue)"/>
    <path d="M0 0H160C100 6 40 18 0 34Z" fill="var(--navy)"/>
  </svg>
  <svg class="swoosh" style="left:0;bottom:0" width="400" height="60" viewBox="0 0 400 60">
    <path d="M0 60H400V10C300 40 150 50 0 46Z" fill="var(--sky)"/>
    <path d="M0 60H400V22C300 48 150 56 0 54Z" fill="var(--blue)"/>
    <path d="M180 60H400V38C330 52 260 58 180 60Z" fill="var(--green)"/>
  </svg>
  <div class="head" style="margin-top:18px">
    <div>
      <div class="brand"><span class="brand-dot"></span><span class="brand-name">MAPLEGATE ELECTRIC</span></div>
      <div class="brand-sub">1865 Quillon Ridge San Antonio. TX 78299</div>
    </div>
    <div class="contact-block">210.555.0187 x240<br>pwinter@qbn.example<br>www.qbn.example<br>Corporate Headquarters Houston TX</div>
  </div>
  <div class="letter-body">
    <p>Date</p>
    <p>Name of Recipient<br>Address</p>
    <p>Dear Sir/Madam</p>
    <p>We are pleased to confirm the scheduled electrical service for your facility. Our licensed crew will arrive on the agreed date and complete the inspection, panel upgrades and safety testing. A detailed report will follow within two business days, along with recommendations for any further work required.</p>
    <p>Should you have questions about the schedule or scope, please contact our office directly. We value your trust and look forward to serving you.</p>
    <p>Sincerely</p>
    <div class="signature">Paula Winter</div>
    <p>Paula Winter<br>VP Sales &amp; Marketing</p>
  </div>
</section>

<!-- Letterhead, right: footer variant -->
<section class="piece letterhead" style="left:836px;top:24px;width:340px;height:500px">
  <div class="head">
    <div>
      <div class="brand"><span class="brand-dot"></span><span class="brand-name">MAPLEGATE ELECTRIC</span></div>
      <div class="brand-sub">1865 Quillon Ridge San Antonio. TX 78299</div>
    </div>
    <div class="contact-block">210.555.0187 x240<br>pwinter@qbn.example<br>www.qbn.example</div>
  </div>
  <div class="letter-body">
    <p>Date</p>
    <p>Name of Recipient<br>Address</p>
    <p>Dear Sir/Madam</p>
    <p>We are pleased to confirm the scheduled electrical service for your facility. Our licensed crew will arrive on the agreed date and complete the inspection, panel upgrades and safety testing. A detailed report will follow within two business days, along with recommendations for any further work required.</p>
    <p>Should you have questions about the schedule or scope, please contact our office directly. We value your trust and look forward to serving you.</p>
    <p>Sincerely</p>
    <div class="signature">Paula Winter</div>
    <p>Paula Winter<br>VP Sales &amp; Marketing</p>
  </div>
  <svg class="swoosh" style="left:0;bottom:24px" width="340" height="6" viewBox="0 0 340 6">
    <rect x="22" y="2" width="296" height="1.5" fill="var(--blue)"/>
  </svg>
  <div class="footer-line">Corporate Headquarters Houston TX · ISO 9001 Certified Quality Management System</div>
</section>

<!-- Small envelope, centre -->
<section class="piece envelope envelope-small" style="left:590px;top:466px;width:230px;height:76px">
  <svg class="swoosh" style="left:0;bottom:0" width="230" height="24" viewBox="0 0 230 24">
    <path d="M0 24H230V4C160 18 80 22 0 20Z" fill="var(--blue)"/>
    <path d="M110 24H230V14C190 22 150 24 110 24Z" fill="var(--green)"/>
  </svg>
  <div class="brand"><span class="brand-dot"></span><span class="brand-name">MAPLEGATE ELECTRIC</span></div>
</section>

<!-- Left business cards + envelope -->
<section class="piece envelope" style="left:24px;top:664px;width:440px;height:176px">
  <div class="brand" style="margin-top:40px"><span class="brand-dot"></span><span class="brand-name">MAPLEGATE ELECTRIC</span></div>
  <div class="brand-sub">1865 Quillon Ridge San Antonio. TX 78299</div>
  <div class="recipient">Name of Recipient<br>Address</div>
</section>
<section class="piece card" style="left:24px;top:548px;width:190px;height:108px">
  <div class="holder">Paula Winter</div>
  <div class="role">VP Sales &amp; Marketing</div>
  <div class="details">210.555.0187 x240<br>pwinter@qbn.example<br>www.qbn.example</div>
  <div class="hq">Corporate Headquarters Houston TX</div>
</section>
<section class="piece card" style="left:222px;top:548px;width:190px;height:108px">
  <div class="brand brand-mid"><span class="brand-dot"></span><span class="brand-name">MAPLEGATE ELECTRIC</span></div>
  <div class="brand-sub">1865 Quillon Ridge San Antonio. TX 78299</div>
  <div class="iso">ISO 9001 Certified Quality Management System</div>
</section>

<!-- Centre card grid -->
<section class="piece card card-back card-steel" style="left:492px;top:590px;width:150px;height:82px" role="img" aria-label="Brushed metal card back with company symbol">
  <span class="big-dot"></span><span class="web">www.qbn.example</span>
</section>
<section class="piece card card-back card-steel" style="left:652px;top:590px;width:150px;height:82px" role="img" aria-label="Brushed metal card back with company symbol">
  <span class="big-dot"></span><span class="web">www.qbn.example</span>
</section>
<section class="piece card card-back" style="left:492px;top:680px;width:150px;height:82px">
  <div class="brand brand-compact"><span class="brand-dot"></span><span class="brand-name">MAPLEGATE ELECTRIC</span></div>
  <span class="web">www.qbn.example</span>
</section>
<section class="piece card card-back" style="left:652px;top:680px;width:150px;height:82px">
  <div class="brand brand-compact"><span class="brand-dot"></span><span class="brand-name">MAPLEGATE ELECTRIC</span></div>
  <span class="web">www.qbn.example</span>
</section>
<section class="piece card" style="left:492px;top:770px;width:150px;height:80px">
  <div class="holder">Paula Winter</div>
  <div class="role">VP Sales &amp; Marketing</div>
  <div class="details">210.555.0187 x240<br>pwinter@qbn.example</div>
</section>
<section class="piece card" style="left:652px;top:770px;width:150px;height:80px">
  <div class="brand brand-compact"><span class="brand-dot"></span><span class="brand-name">MAPLEGATE ELECTRIC</span></div>
  <div class="brand-sub">1865 Quillon Ridge San Antonio. TX 78299</div>
</section>

<!-- Right business cards + envelope -->
<section class="piece envelope" style="left:814px;top:664px;width:366px;height:176px">
  <svg class="swoosh" style="left:0;bottom:0" width="366" height="40" viewBox="0 0 366 40">
    <path d="M0 40H366V6C260 30 125 38 0 34Z" fill="var(--blue)"/>
    <path d="M180 40H366V22C305 36 240 40 180 40Z" fill="var(--green)"/>
  </svg>
  <div class="brand" style="margin-top:40px"><span class="brand-dot"></span><span class="brand-name">MAPLEGATE ELECTRIC</span></div>
  <div class="brand-sub">1865 Quillon Ridge San Antonio. TX 78299</div>
  <div class="recipient">Name of Recipient<br>Address</div>
</section>
<section class="piece card" style="left:818px;top:548px;width:172px;height:104px">
  <div class="holder">Paula Winter</div>
  <div class="role">VP Sales &amp; Marketing</div>
  <div class="details">210.555.0187 x240<br>pwinter@qbn.example<br>www.qbn.example</div>
  <svg class="swoosh" style="left:0;bottom:0" width="172" height="14" viewBox="0 0 172 14">
    <path d="M0 14H172V2C115 10 57 13 0 12Z" fill="var(--blue)"/>
  </svg>
</section>
<section class="piece card" style="left:1000px;top:548px;width:172px;height:104px">
  <div class="brand brand-mid"><span class="brand-dot"></span><span class="brand-name">MAPLEGATE ELECTRIC</span></div>
  <div class="brand-sub">1865 Quillon Ridge San Antonio. TX 78299</div>
  <div class="iso" style="bottom:18px">ISO 9001 Certified Quality Management System</div>
  <svg class="swoosh" style="left:0;bottom:0" width="172" height="14" viewBox="0 0 172 14">
    <path d="M0 14H172V2C115 10 57 13 0 12Z" fill="var(--green)"/>
  </svg>
</section>

</body>
</html>
```